Seasoned logs and kindling for sale

producing firewood from beech,ash,oak and silver birch,
Kindling is produce from a variety of seasoned softwoods

Industry/Entity Type

Firewood

Contact Information for Business Card

mark Pellew 07812603948
dave Tillard 07846217035
e-mail,markp318@mailbrook.net

```html
<!DOCTYPE html>
<html lang="en">
<head>
<meta charset="utf-8">
<title>Firewood Business Card</title>
<link rel="stylesheet" href="https://fonts.googleapis.com/css2?family=Questrial&display=swap">
<style>
  :root {
    --card-black: #000000;
    --band-orange: #f07022;
    --band-edge: #f6a04a;
    --title-gold: #f2a81d;
    --text-white: #ffffff;
    --divider: #3a3a3a;
    --flame-dark: #1a0a02;
    --flame-deep: #6b2a06;
    --flame-mid: #d7731a;
    --flame-bright: #f7c068;
  }
  html, body {
    margin: 0;
    padding: 0;
    overflow: hidden;
    background: #ffffff;
  }
  .card {
    position: relative;
    width: 1200px;
    height: 693px;
    background: var(--card-black);
    overflow: hidden;
    font-family: "Questrial", "Century Gothic", sans-serif;
    color: var(--text-white);
  }
  .hero-fire {
    position: absolute;
    left: 0;
    top: 0;
    width: 1200px;
    height: 252px;
    background:
      radial-gradient(ellipse 220px 140px at 140px 90px, var(--flame-bright) 0%, var(--flame-mid) 45%, transparent 75%),
      radial-gradient(ellipse 260px 150px at 470px 70px, var(--flame-bright) 0%, var(--flame-mid) 40%, transparent 75%),
      radial-gradient(ellipse 240px 130px at 900px 80px, var(--flame-bright) 0%, var(--flame-mid) 45%, transparent 75%),
      radial-gradient(ellipse 200px 120px at 1150px 120px, var(--flame-mid) 0%, transparent 70%),
      linear-gradient(180deg, var(--flame-deep) 0%, var(--flame-dark) 100%);
  }
  .accent-band {
    position: absolute;
    left: 0;
    top: 252px;
    width: 1200px;
    height: 44px;
    background: var(--band-orange);
    border-bottom: 3px solid var(--band-edge);
  }
  .company-name {
    position: absolute;
    left: 0;
    width: 1200px;
    top: 334px;
    margin: 0;
    text-align: center;
    font-size: 47px;
    font-weight: 400;
    color: var(--title-gold);
    letter-spacing: 0.5px;
  }
  .contact {
    position: absolute;
    top: 458px;
    font-size: 32px;
    line-height: 48px;
    margin: 0;
  }
  .contact-left { left: 130px; text-align: left; }
  .contact-right { right: 143px; text-align: right; }
  .contact-divider {
    position: absolute;
    left: 605px;
    top: 465px;
    width: 1px;
    height: 88px;
    background: var(--divider);
  }
  .email {
    position: absolute;
    left: 0;
    width: 1200px;
    top: 611px;
    margin: 0;
    text-align: center;
    font-size: 27px;
  }
</style>
</head>
<body>
  <div class="card">
    <div class="hero-fire" role="img" aria-label="Photograph of burning logs with bright orange flames"></div>
    <div class="accent-band"></div>
    <h1 class="company-name">Company name</h1>
    <p class="contact contact-left">Mark Pellew<br>07812603948</p>
    <div class="contact-divider"></div>
    <p class="contact contact-right">Dave Tillard<br>07846217035</p>
    <p class="email">E-mail: markp318@mailbrook.net</p>
  </div>
</body>
</html>
```